Postcard Design

Name of Company: PRAIRIE DWELLING BROKERS - A NEW AND RESALE MANUFACTURED HOME COMPANY, AID IN THE PURCHASE OR SELL OF NEW AND USED MOBILEHOMES, HAVE OVER 30 YEARS IN THE REAL ESTATE INDUSTRY,
WE OFFER A FREE HOME INSPECTION WITH EVERY NEW LISTING A $250.00 VALUE SO YOU KNOW THE HEALTH AND SAFETY STATUS OF YOUR HOME SO THERE ARE NO SURPRISES WHEN YOU ARE READY TO CLOSE THE SALE OF YOUR HOME AND HAVE TO GIVE UP THOUSANDS OF DOLLARS IN REPAIRS.

"COUPON" GOOD FOR $2,000.00 OFF SALES COMMISSION
WE BUY MOBILEHOMES

Check out our site for more information:
prairiedwellingbrokers.example

Target Market(s)

MOBILEHOME OWNERS/ BUYERS

Industry/Entity Type

Real Estate

Colors
00a990
00a98f
86cfc6
33a6d7
3276b5

Requirements
Must have
• CAN WE USE TWO SIDES OF POST CARD

```html
<!DOCTYPE html>
<html lang="en">
<head>
<meta charset="utf-8">
<title>Prairie Dwelling Brokers – Postcard</title>
<link rel="stylesheet" href="https://fonts.googleapis.com/css2?family=Oswald:wght@300;400;600&family=Quicksand:wght@700&display=swap">
<style>
  :root {
    --card-frame: #ffffff;
    --field-teal: #86cfc6;
    --panel-green: #00a98f;
    --coupon-fill: #3dbaa5;
    --text-light: #ffffff;
    --brand-navy: #1f3a6b;
    --photo-sky: #dfe7e4;
    --photo-hill: #6f7a4e;
    --photo-road: #5b5e5c;
    --shadow: rgba(0, 0, 0, 0.28);
  }
  * { margin: 0; padding: 0; box-sizing: border-box; }
  html, body {
    width: 1200px; height: 958px; overflow: hidden;
    background: #f4f4f2;
  }
  .postcard {
    position: relative;
    width: 1200px; height: 958px;
    background: var(--field-teal);
    border: 16px solid var(--card-frame);
    overflow: hidden;
    font-family: "Oswald", "Arial Narrow", sans-serif;
    color: var(--text-light);
  }
  .postcard > * { position: absolute; }
  .panel-shape { left: -16px; top: -16px; width: 1200px; height: 958px; }
  .headline {
    left: 78px; top: 84px;
    font-weight: 300;
    font-size: 43px; line-height: 69px;
    letter-spacing: 0.5px;
    text-transform: uppercase;
  }
  .photo-stack { left: 431px; top: 105px; width: 661px; height: 470px; }
  .photo-stack .print {
    position: absolute; inset: 0;
    background: var(--card-frame);
    box-shadow: 0 3px 10px var(--shadow);
  }
  .print.back-one { transform: rotate(-3.5deg); }
  .print.back-two { transform: rotate(2.5deg); }
  .print.front { padding: 14px; }
  .photo-area {
    width: 100%; height: 100%;
    background:
      linear-gradient(to bottom, transparent 62%, var(--photo-road) 62%, #4b4e4c 100%),
      linear-gradient(to bottom, var(--photo-sky) 0%, #b9bfa7 25%, var(--photo-hill) 45%, #8a7a55 62%);
  }
  .tagline {
    left: 464px; top: 448px;
    font-family: "Quicksand", "Trebuchet MS", sans-serif;
    font-weight: 700;
    font-size: 50px; line-height: 56px;
    text-shadow: 2px 3px 4px rgba(0,0,0,0.6);
  }
  .tagline .small { font-size: 42px; }
  .coupon {
    left: 109px; top: 634px; width: 566px; height: 56px;
    background: var(--coupon-fill);
    border: 2px dashed var(--text-light);
    border-right: none;
    display: flex; align-items: center; justify-content: center;
    font-size: 30px; font-weight: 400;
  }
  .experience {
    left: 60px; top: 722px; width: 580px;
    text-align: center; text-transform: uppercase;
    font-weight: 400;
  }
  .experience .lead { font-size: 35px; line-height: 48px; }
  .experience .lead strong { font-weight: 600; font-size: 39px; }
  .experience .sub { font-size: 29px; line-height: 40px; }
  .brand {
    left: 760px; top: 660px; width: 340px; height: 160px;
    display: flex; align-items: center; gap: 16px;
  }
  .brand .mark { width: 30px; height: 30px; background: var(--brand-navy); flex: none; }
  .brand .name {
    color: var(--brand-navy);
    font-weight: 600; font-size: 38px; line-height: 44px;
    text-transform: uppercase;
  }
  .contact-row {
    left: 80px; top: 850px; right: 20px;
    display: flex; align-items: center;
    font-size: 30px;
  }
  .contact-row .call { font-weight: 600; margin-right: 52px; }
  .contact-row svg { width: 40px; height: 40px; margin-right: 12px; flex: none; }
  .contact-row .phone { margin-right: 46px; }
  .contact-row .web { font-size: 26px; }
</style>
</head>
<body>
<main class="postcard">
  <svg class="panel-shape" viewBox="0 0 1200 958" aria-hidden="true">
    <path d="M58 55 H600 C652 55 691 97 691 150 V709 H180 C112 709 58 655 58 590 Z" fill="var(--panel-green)"/>
  </svg>

  <h1 class="headline">A new &amp; resale<br>manufactured<br>home company<br>aid in the<br>purchase or sell<br>of the new &amp; used<br>mobilehomes</h1>

  <div class="photo-stack">
    <div class="print back-one"></div>
    <div class="print back-two"></div>
    <div class="print front">
      <div class="photo-area" role="img" aria-label="Photo of a white mobile home carrying a wide load sign being transported on a winding hillside road"></div>
    </div>
  </div>

  <p class="tagline">“We <span class="small">BUY</span><br><span class="small">mobilehomes</span>”</p>

  <p class="coupon">$2,000.00 OFF ON SALES COMMISSION</p>

  <div class="experience">
    <p class="lead">Over <strong>30 years of experience</strong></p>
    <p class="sub">in the real estate industry</p>
  </div>

  <div class="brand">
    <span class="mark"></span>
    <span class="name">Prairie Dwelling<br>Brokers</span>
  </div>

  <div class="contact-row">
    <span class="call">CALL TODAY:</span>
    <svg viewBox="0 0 40 40" aria-hidden="true">
      <circle cx="20" cy="20" r="17" fill="none" stroke="#fff" stroke-width="2"/>
      <path d="M14 11 l4 0 l1 6 l-3 2 c1 3 3 5 6 6 l2-3 l6 1 l0 4 c-9 1 -17 -7 -16 -16z" fill="none" stroke="#fff" stroke-width="1.8" stroke-linejoin="round"/>
    </svg>
    <span class="phone">555 010 4827</span>
    <svg viewBox="0 0 40 40" aria-hidden="true">
      <g fill="none" stroke="#fff" stroke-width="2">
        <circle cx="20" cy="20" r="16"/>
        <ellipse cx="20" cy="20" rx="7" ry="16"/>
        <line x1="4" y1="20" x2="36" y2="20"/>
        <path d="M7 12 H33 M7 28 H33"/>
      </g>
    </svg>
    <span class="web">www.prairiedwellingbrokers.example</span>
  </div>
</main>
</body>
</html>
```